Quillbrook Health needs a new services brochure

We need a new brochure that highlights the services that we offer at our clinic. We are a multidisciplinary health clinic that focuses on injury rehabilitation and pain management. We are looking for a brochure that will highlight our primary services to our clientele and inform potential clients of what we can offer. We pride ourselves on our quality of care and our advanced treatment techniques.
Target Market(s)
young families, athletes, people interested in their health.
Industry/Entity Type
Health And Wellness
Colors
Designer to choose colors to be used in the design.
Requirements
Must have
- We would love our new brochure to be a tri-fold that has 6 pages. We would like it to have brief information about our featured services:
- - Chiropractic
- - Massage Therapy
- - Manual Osteopathic Therapy
- - Acupuncture
- - Laser Therapy
- - Radial Shockwave Therapy
- We would also like this brochure to include a brief price list and direct billing info, About Us section & Contact information.
Nice to have
- If there is space to list that we also offer other services such as : Tissue Unwind Method, Hot Stone Massage, Cupping Technique, Pembrill Method, and Kinesiology Taping that would be great. We would like to use images similar to those that are on our website (we have hi-res of all images on the website) www.quillbrookhealth.ca and colours that would fit with our logo.

```html
<!DOCTYPE html>
<html lang="en">
<head>
<meta charset="utf-8">
<title>Quillbrook Health – Services Brochure</title>
<link rel="stylesheet" href="https://fonts.googleapis.com/css2?family=Ubuntu:wght@500;700&family=Mulish:ital,wght@0,300;0,400;0,600;1,300;1,400;1,700&display=swap">
<style>
:root{
  --page:#d6d6d8;
  --panel:#222326;
  --panel-dark:#17181a;
  --ink:#e6e7ea;
  --muted:#b9bcc3;
  --accent:#3f78c4;
  --accent-soft:#6d9ad6;
  --photo-a:#1d3a5f;
  --photo-b:#5b86b8;
  --photo-c:#9fbde0;
}
*{box-sizing:border-box;margin:0;padding:0}
html,body{width:1200px;height:960px;overflow:hidden}
body{background:var(--page);font-family:"Mulish",sans-serif;color:var(--ink);position:relative}
.brochure{position:absolute;left:30px;top:40px;width:1140px;height:880px;display:flex;box-shadow:0 10px 30px rgba(0,0,0,.25)}
.panel{width:380px;height:880px;position:relative;background:linear-gradient(180deg,var(--panel) 0%,var(--panel-dark) 100%);overflow:hidden}
.panel + .panel{border-left:1px solid rgba(255,255,255,.06)}
h2{font-family:"Ubuntu",sans-serif;font-weight:700;font-style:italic;color:var(--accent-soft);font-size:24px;letter-spacing:.5px}
h3{font-family:"Mulish",sans-serif;font-weight:700;color:var(--accent);font-size:14px;margin-top:14px;margin-bottom:3px}
.pricing{padding:40px 34px}
.pricing .note{font-size:9px;color:var(--muted);margin:4px 0 6px;font-style:italic}
.row{display:flex;align-items:baseline;font-size:13px;line-height:1.45;color:var(--ink);font-weight:300}
.row .dots{flex:1;border-bottom:1px dotted var(--muted);margin:0 4px;transform:translateY(-3px)}
.row .price{min-width:44px;text-align:right}
.row .price2{min-width:44px;text-align:right}
.colhead{display:flex;justify-content:flex-end;font-size:9px;color:var(--muted);gap:18px;padding-right:4px}
.plain{font-size:13px;font-weight:300;line-height:1.5}
.billing{padding:40px 30px 0}
.billing p{font-size:11.5px;line-height:1.42;font-weight:300;font-style:italic;margin-top:10px;position:relative;z-index:1}
.billing strong{font-weight:700;color:#fff}
.insurers{display:grid;grid-template-columns:1fr 1fr;font-size:11.5px;font-style:italic;font-weight:300;line-height:1.45;margin:8px 0 0 14px;position:relative;z-index:1}
.photo-mid{position:absolute;left:0;top:320px;width:380px;height:290px;background:linear-gradient(160deg,var(--photo-c) 0%,var(--photo-b) 45%,var(--photo-a) 100%);opacity:.85}
.location{position:absolute;left:30px;top:650px;right:30px}
.location h3{font-style:italic;font-size:14px}
.location p{font-size:12px;font-style:italic;font-weight:300;line-height:1.45;margin-bottom:14px}
.contact{font-size:12px;font-style:italic;line-height:1.6}
.contact .lbl{color:var(--accent)}
.contact .web{color:var(--accent)}
.cover .headline{position:absolute;left:0;right:36px;top:150px;text-align:right;font-family:"Ubuntu",sans-serif;font-weight:700;font-size:46px;line-height:1.05}
.headline .l1{color:#fff;display:block}
.headline .l2{color:var(--accent);display:block}
.photo-cover{position:absolute;left:0;top:290px;width:380px;height:330px;background:linear-gradient(200deg,var(--photo-c) 0%,var(--photo-b) 40%,var(--photo-a) 100%);opacity:.85}
.tagline{position:absolute;left:40px;right:30px;top:540px;font-family:"Ubuntu",sans-serif;font-weight:700;font-size:17px;line-height:1.3;color:#fff}
.brand{position:absolute;left:40px;bottom:80px;display:flex;align-items:center;gap:12px}
.brand .dot{width:34px;height:34px;border-radius:50%;background:var(--accent)}
.brand .name{font-family:"Mulish",sans-serif;font-weight:600;font-size:30px;color:var(--accent)}
</style>
</head>
<body>
<div class="brochure">

  <section class="panel pricing">
    <h2>Pricing</h2>
    <p class="note">GST will be added to all applicable services: Massage, Shockwave, Laser</p>

    <h3>Massage Therapy</h3>
    <div class="row"><span>30 Minute</span><span class="dots"></span><span class="price">$50</span></div>
    <div class="row"><span>45 Minute</span><span class="dots"></span><span class="price">$75</span></div>
    <div class="row"><span>60 Minute</span><span class="dots"></span><span class="price">$90</span></div>
    <div class="row"><span>90 Minute</span><span class="dots"></span><span class="price">$130</span></div>
    <div class="row"><span>Infant Massage Instruction</span><span class="dots"></span><span class="price">$50</span></div>
    <div class="row"><span>Hot Stone Addition (+$20 to regular treatment price)</span></div>

    <h3>Chiropractic</h3>
    <div class="colhead"><span>initial</span><span>subsequent</span></div>
    <div class="row"><span>Pediatrics 0–5 yr old</span><span class="dots"></span><span class="price">$115</span><span class="price2">$55</span></div>
    <div class="row"><span>Student (6+ yrs, full time)</span><span class="dots"></span><span class="price">$115</span><span class="price2">$55</span></div>
    <div class="row"><span>Adult</span><span class="dots"></span><span class="price">$125</span><span class="price2">$65</span></div>
    <div class="row"><span>Senior 65+ yrs</span><span class="dots"></span><span class="price">$115</span><span class="price2">$55</span></div>
    <div class="row"><span>Chiropractic and laser treatment</span><span class="dots"></span><span class="price"></span><span class="price2">$95</span></div>
    <div class="row"><span>Chiropractic and shockwave therapy</span><span class="dots"></span><span class="price"></span><span class="price2">$95</span></div>

    <h3>Acupuncture</h3>
    <div class="row"><span>Initial Assessment and Treatment</span><span class="dots"></span><span class="price">$120</span></div>
    <div class="row"><span>Subsequent Treatment</span><span class="dots"></span><span class="price">$85</span></div>

    <h3>Manual Osteopathic Therapy</h3>
    <div class="row"><span>Initial Assessment and Treatment</span><span class="dots"></span><span class="price">$150</span></div>
    <div class="row"><span>Subsequent Treatment</span><span class="dots"></span><span class="price">$120</span></div>

    <h3>Laser Therapy</h3>
    <div class="row"><span>Initial Assessment and Treatment</span><span class="dots"></span><span class="price">$90</span></div>
    <div class="row"><span>Subsequent Treatments</span><span class="dots"></span><span class="price">$50</span></div>

    <h3>Shockwave Therapy</h3>
    <div class="row"><span>Initial Assessment and Treatment</span><span class="dots"></span><span class="price">$90</span></div>
    <div class="row"><span>Subsequent Treatments</span><span class="dots"></span><span class="price">$75</span></div>

    <h3>Pembrill Method</h3>
    <p class="plain">Included with chiropractic treatment with Dr. Halden and Dr. Rosset and massage therapy with Theo.</p>

    <h3>Cupping Technique</h3>
    <p class="plain">Included with massage therapy with Theo and Marla and acupuncture with Dr. Linnea.</p>
  </section>

  <section class="panel billing">
    <div class="photo-mid" role="img" aria-label="Blue-toned photo of an active woman stretching outdoors"></div>
    <h2>Direct Billing</h2>
    <p>We are happy to offer direct billing to extended healthcare plans which allow direct billing and online claim submissions from providers.</p>
    <p>As all insurance companies and plans are different, we recommend asking your plan provider directly if they allow online direct billing on your specific plan. Unfortunately at this time, insurance companies do not allow an option for direct billing for Manual Osteopathy, except in the case of Evergreen Cover and Prairie Shield. Most insurance plans do allow patients to submit manual osteopathy claims online and if you are set up for direct deposit, most plans will deposit claim payments within 48 hours.</p>
    <p>The following insurance companies typically allow online direct billing:</p>
    <div class="insurers">
      <span>Prairie Shield Benefits</span><span>Merchants Alliance</span>
      <span>Halvor Group</span><span>Coteau Mutual</span>
      <span>Northstar Life</span><span>Evergreen Cover</span>
      <span>Meridian Financial</span><span>Tallis</span>
      <span>Tallis Group</span><span>Harborline</span>
      <span>Keystone Benefit</span><span>Common Life</span>
      <span>Brightway Life</span><span></span>
    </div>
    <p>Occasionally some insurance companies will conduct random audits on claims or send claims for further processing. <strong>In these instances, we are unable to direct bill for that individual claim.</strong> The insurance company will send payment directly to you once the claim has been processed.</p>

    <div class="location">
      <h3>Fernhill Commons</h3>
      <p>We are located on the 2nd floor of the professional building beside Harbour Grocer. Elevator or stair access is from the main lobby beside Fernhill Optical.</p>
      <div class="contact">
        <div>4120 - 1880 Larkspur Ridge Way NW</div>
        <div>Brookton, AB T0X 1Q2</div>
        <div><span class="lbl">t</span> (555) 201-4470 &nbsp; <span class="lbl">e</span> info@quillbrookhealth.ca</div>
        <div class="web">www.quillbrookhealth.ca</div>
      </div>
    </div>
  </section>

  <section class="panel cover">
    <div class="photo-cover" role="img" aria-label="Blue-toned photo of a woman in athletic wear stretching her shoulder"></div>
    <h1 class="headline"><span class="l1">Live life</span><span class="l2">pain free</span></h1>
    <p class="tagline">Helping you get back to enjoying a healthy, active life.</p>
    <div class="brand">
      <span class="dot"></span>
      <span class="name">Quillbrook Health</span>
    </div>
  </section>

</div>
</body>
</html>
```